Boutique Sparkling Blanc de Blancs Wine label

We are looking for a label and neck label for our new Sparkling Chardonnay.
Images uploaded include, bubbles and glitter maybe as a faded background for whole label?
We like Refined, elegant yet simple designs.
Have included our current table chardonnay label as example.

Industry/Entity Type

Boutique

Font styles to use
Decorative
Script

Requirements
Must have
• Name - "Beneath the Lanterns"
• Methode Traditionelle
• Blanc de Blancs
• 2015
• Across the Orchard (Brand)
• Adelaide Hills
Nice to have
• Neutral tones
• Sparkles, Glitter, Bubbles
• Traditional, cursive or vine like fonts
• Have attached fonts we used for previous wine label - might be nice to carry through same/similar fonts to continue our brand?
Should not have
• a lot of colour

```html
<!DOCTYPE html>
<html lang="en">
<head>
<meta charset="utf-8">
<title>Beneath the Lanterns – Sparkling Label</title>
<link rel="stylesheet" href="https://fonts.googleapis.com/css2?family=Great+Vibes&family=Cinzel:wght@400;600&display=swap">
<style>
  :root {
    --backdrop: #ececec;
    --label-green: #0e4a1c;
    --label-deep: #03170a;
    --label-black: #050805;
    --gold: #d8b44a;
    --gold-light: #f3dc86;
    --gold-dark: #8f6a1c;
    --foil: #141414;
  }
  * { margin: 0; padding: 0; box-sizing: border-box; }
  html, body {
    width: 801px;
    height: 1200px;
    overflow: hidden;
    background: var(--backdrop);
  }
  .canvas {
    position: relative;
    width: 801px;
    height: 1200px;
  }
  .front-label {
    position: absolute;
    left: 50px;
    top: 120px;
    width: 700px;
    height: 700px;
  }
  .front-label .wine-name {
    font-family: "Great Vibes", cursive;
    fill: var(--gold);
  }
  .front-label .details {
    font-family: "Cinzel", serif;
    fill: var(--gold);
    font-size: 13.5px;
    letter-spacing: 1.4px;
  }
  .front-label .vintage {
    font-family: "Cinzel", serif;
    font-weight: 600;
    fill: var(--gold);
    font-size: 16px;
    letter-spacing: 1.5px;
  }
  .neck-label {
    position: absolute;
    left: 150px;
    top: 920px;
    width: 500px;
    height: 84px;
    background: var(--foil);
    border-top: 3px solid var(--gold);
    border-bottom: 3px solid var(--gold);
    display: flex;
    align-items: center;
    justify-content: center;
  }
  .neck-label .brand-name {
    font-family: "Cinzel", serif;
    font-size: 22px;
    letter-spacing: 3px;
    color: var(--gold);
  }
</style>
</head>
<body>
<main class="canvas">
  <svg class="front-label" viewBox="0 0 448 448" aria-label="Front label">
    <defs>
      <radialGradient id="label-fill" cx="50%" cy="48%" r="60%">
        <stop offset="0" stop-color="var(--label-green)"/>
        <stop offset="0.65" stop-color="var(--label-deep)"/>
        <stop offset="1" stop-color="var(--label-black)"/>
      </radialGradient>
      <linearGradient id="gold-line" x1="0" y1="0" x2="1" y2="1">
        <stop offset="0" stop-color="var(--gold-dark)"/>
        <stop offset="0.5" stop-color="var(--gold-light)"/>
        <stop offset="1" stop-color="var(--gold-dark)"/>
      </linearGradient>
      <linearGradient id="vine-tone" x1="0" y1="0" x2="1" y2="0">
        <stop offset="0" stop-color="var(--gold)" stop-opacity="0"/>
        <stop offset="0.2" stop-color="var(--gold)" stop-opacity="0.55"/>
        <stop offset="0.5" stop-color="var(--gold-light)" stop-opacity="0.75"/>
        <stop offset="0.8" stop-color="var(--gold)" stop-opacity="0.55"/>
        <stop offset="1" stop-color="var(--gold)" stop-opacity="0"/>
      </linearGradient>
      <path id="label-outline" d="M105,160 L105,120 A119,119 0 0 1 343,120 L343,160 Q346,165 356,165 L418,165 L448,205 L448,382 Q448,390 438,393 L224,448 L10,393 Q0,390 0,382 L0,205 L30,165 L92,165 Q102,165 105,160 Z"/>
    </defs>

    <use class="label-body" href="#label-outline" fill="url(#label-fill)"/>
    <use class="label-frame" href="#label-outline" fill="none" stroke="url(#gold-line)" stroke-width="3.2"
         transform="translate(224 224) scale(0.955) translate(-224 -224)"/>

    <rect class="crest-ornament" role="img" aria-label="Small gold scroll ornament" x="160" y="32" width="128" height="28" rx="14" fill="url(#vine-tone)"/>

    <text class="wine-name" x="224" y="108" text-anchor="middle" font-size="40">Beneath the</text>
    <text class="wine-name" x="224" y="150" text-anchor="middle" font-size="40">Lanterns</text>

    <rect class="vine-ornament" role="img" aria-label="Gold grapevine border with leaves and grape clusters" x="30" y="185" width="388" height="50" rx="25" fill="url(#vine-tone)"/>

    <text class="details" x="224" y="268" text-anchor="middle">METHODE TRADITIONELLE</text>
    <text class="details" x="224" y="291" text-anchor="middle">BLANC DE BLANCS</text>
    <text class="details" x="224" y="314" text-anchor="middle">ADELAIDE HILLS</text>

    <rect class="vine-ornament" role="img" aria-label="Gold grapevine border with leaves and grape clusters" x="30" y="333" width="388" height="50" rx="25" fill="url(#vine-tone)"/>

    <text class="vintage" x="224" y="411" text-anchor="middle">2015</text>
  </svg>

  <div class="neck-label">
    <span class="brand-name">ACROSS THE ORCHARD</span>
  </div>
</main>
</body>
</html>
```